Plastering (solid plastering) business card design

We need a business card for a a small plastering business based in Perth Western Australia. We are a small team that provides a service in solid plastering specialising in float, white set and sand finish. We would like to see a clean business card with our name "Brightline Plastering" being the focus of the card and maybe incorporated into a logo. We don't have a logo at the moment so we would like to see some cards that may provide us with our future logo.

Industry/Entity Type

Business

Contact Information for Business Card

Brightline Plastering

Solid Plastering Specialists

Ph: Corey 0417683091
Ph: Liam 0468120357

Requirements
Should not have
• The design should not have Drywall incorporated into the card. In perth W.A. Plastering in different to someone that puts up Plyvane. We use sand, cement, lime and hardwall plaster.

```html
<!DOCTYPE html>
<html lang="en">
<head>
<meta charset="utf-8">
<title>Brightline Plastering – Business Card</title>
<link rel="stylesheet" href="https://fonts.googleapis.com/css2?family=Montserrat:wght@300;400&display=swap">
<style>
  :root {
    --page-bg: #d9d9d9;
    --charcoal: #39383b;
    --coral: #f07362;
    --white: #ffffff;
    --ink: #2e2d30;
    --fold: #b9b9b9;
    --ghost: rgba(240, 115, 98, 0.16);
  }
  * { margin: 0; padding: 0; box-sizing: border-box; }
  html, body {
    width: 1200px;
    height: 900px;
    overflow: hidden;
    background: var(--page-bg);
    font-family: "Montserrat", sans-serif;
  }
  .stage {
    width: 1200px;
    height: 900px;
    display: flex;
    align-items: center;
    justify-content: center;
  }
  .card {
    position: relative;
    width: 900px;
    height: 514px;
    display: flex;
    box-shadow: 0 10px 30px rgba(0, 0, 0, 0.18);
  }
  .card__contacts {
    position: relative;
    width: 380px;
    background: var(--charcoal);
    color: var(--white);
    padding: 140px 0 0 60px;
    overflow: hidden;
  }
  .card__brand {
    position: relative;
    flex: 1;
    background: var(--coral);
  }
  .contact {
    border-top: 2px solid var(--white);
    padding-top: 10px;
    margin-bottom: 22px;
    font-weight: 300;
  }
  .contact__name {
    font-size: 26px;
    letter-spacing: 1px;
    text-transform: uppercase;
    line-height: 1.1;
  }
  .contact__phone {
    display: flex;
    align-items: center;
    gap: 8px;
    font-size: 28px;
    letter-spacing: 1.5px;
    line-height: 1.2;
  }
  .contact__phone svg { width: 22px; height: 22px; flex: none; }
  .contact--second { margin-left: 12px; }
  .card__ghost-name {
    position: absolute;
    left: 60px;
    bottom: 90px;
    font-size: 30px;
    font-weight: 300;
    color: var(--ghost);
    text-transform: uppercase;
    letter-spacing: 2px;
  }
  .brand__mark {
    position: absolute;
    left: 215px;
    top: 110px;
    width: 110px;
    height: 110px;
    border-radius: 50%;
    background: var(--charcoal);
  }
  .brand__name {
    position: absolute;
    left: 0;
    right: 0;
    top: 238px;
    text-align: center;
    color: var(--white);
    font-weight: 300;
    font-size: 28px;
    letter-spacing: 1px;
    text-transform: uppercase;
  }
  .ribbon {
    position: absolute;
    left: 350px;
    right: 0;
    top: 284px;
    height: 44px;
    background: var(--white);
    color: var(--ink);
    font-size: 24px;
    font-weight: 400;
    display: flex;
    align-items: center;
    padding-left: 90px;
    z-index: 2;
  }
  .ribbon__fold {
    position: absolute;
    left: 350px;
    top: 328px;
    width: 24px;
    height: 14px;
    z-index: 2;
  }
</style>
</head>
<body>
<main class="stage">
  <article class="card">
    <section class="card__contacts">
      <div class="contact">
        <p class="contact__name">Corey</p>
        <p class="contact__phone">
          <svg viewBox="0 0 24 24" aria-hidden="true"><circle cx="12" cy="12" r="11" fill="#fff"/><path d="M8.2 6.5l1.8-.3 1.1 2.7-1.3 1a7 7 0 0 0 4.3 4.3l1-1.3 2.7 1.1-.3 1.8c-.2.8-1 1.2-1.8 1.1A10 10 0 0 1 7.1 8.3c-.1-.8.3-1.6 1.1-1.8z" fill="#39383b"/></svg>
          0417683091
        </p>
      </div>
      <div class="contact contact--second">
        <p class="contact__name">Liam</p>
        <p class="contact__phone">
          <svg viewBox="0 0 24 24" aria-hidden="true"><circle cx="12" cy="12" r="11" fill="#fff"/><path d="M8.2 6.5l1.8-.3 1.1 2.7-1.3 1a7 7 0 0 0 4.3 4.3l1-1.3 2.7 1.1-.3 1.8c-.2.8-1 1.2-1.8 1.1A10 10 0 0 1 7.1 8.3c-.1-.8.3-1.6 1.1-1.8z" fill="#39383b"/></svg>
          0468120357
        </p>
      </div>
      <p class="card__ghost-name">Brightline</p>
    </section>
    <section class="card__brand">
      <div class="brand__mark" aria-hidden="true"></div>
      <h1 class="brand__name">Brightline Plastering</h1>
    </section>
    <p class="ribbon">Plastering Specialists</p>
    <svg class="ribbon__fold" viewBox="0 0 24 14" aria-hidden="true"><polygon points="0,0 24,0 24,14" fill="var(--fold)"/></svg>
  </article>
</main>
</body>
</html>
```